Website Build for Brindle Media

I want to create a new website for my company. I would like it to be simple, eye catching and punchy. It will be a homepage, a filter section on case studies and a section for a wordpress blog.
Attached is a non-designed image of what I am thinking for the homepage, in terms of structure and wording.
Also attached is an example white paper, so we can follow a similar colour scheme.
Coding
Number of Pages Required
Look and feel

```html
<!DOCTYPE html>
<html lang="en">
<head>
<meta charset="utf-8">
<title>Brindle Media</title>
<link rel="stylesheet" href="https://fonts.googleapis.com/css2?family=Oswald:wght@300;400;500&family=Poppins:wght@300;400;500;600;700&display=swap">
<style>
:root{
  --pink:#e8409a;
  --ink:#151515;
  --text:#333;
  --grey:#f2f2f2;
  --white:#fff;
}
*{margin:0;padding:0;box-sizing:border-box}
html,body{width:1200px;height:3200px;overflow:hidden;background:var(--white)}
body{position:relative;font-family:'Poppins',sans-serif;color:var(--text)}
.abs{position:absolute}
.eyebrow{position:absolute;font:600 15px 'Poppins',sans-serif;color:var(--pink);letter-spacing:.5px}
.btn{position:absolute;background:var(--pink);color:var(--white);font:500 19px 'Oswald',sans-serif;display:flex;align-items:center;justify-content:center;letter-spacing:.5px}

/* brand lockup: plain circle plus name */
.brand{position:absolute;display:flex;align-items:center;gap:14px}
.brand-dot{width:56px;height:56px;border-radius:50%;border:3px solid var(--pink)}
.brand-name{font:500 19px 'Poppins',sans-serif;color:#333}
.brand.on-dark .brand-name{color:var(--white)}

/* header */
.nav a{position:absolute;top:52px;font:500 14px 'Poppins',sans-serif;color:#444;text-decoration:none}
.nav .active{color:var(--pink);border-bottom:2px solid var(--pink);padding-bottom:3px}
.contact-phone{left:840px;top:24px;font:500 25px 'Oswald',sans-serif;color:#222;display:flex;align-items:center;gap:14px}
.contact-mail{left:840px;top:64px;font:500 18px 'Poppins',sans-serif;color:#222;display:flex;align-items:center;gap:14px}

/* hero */
.hero{left:0;top:116px;width:1200px;height:667px}
.hero-photo{position:absolute;inset:0;background:linear-gradient(100deg,#4a4d50 0%,#7d7a72 35%,#b8a98c 60%,#6a5a3e 85%,#3d3a36 100%)}
.hero-title{left:75px;top:244px;font:500 86px/1 'Oswald',sans-serif;color:var(--white);letter-spacing:1px}
.hero-sub{left:75px;top:334px;font:400 27px/33px 'Poppins',sans-serif;color:var(--white)}
.hero-tag{left:75px;top:410px;font:700 22px 'Poppins',sans-serif;color:var(--white);letter-spacing:.5px}
.dots{left:75px;top:546px;display:flex;gap:8px}
.dots i{width:9px;height:9px;border-radius:50%;background:var(--white)}
.dots i.on{background:var(--pink)}

/* about */
.about-photo{left:75px;top:859px;width:422px;height:343px;background:linear-gradient(160deg,#3d4a3a,#6b5c58 50%,#2e3a6a)}
.section-title{position:absolute;font:300 70px/1 'Oswald',sans-serif;color:var(--ink)}
.about-copy{left:525px;top:960px;width:600px;font:400 17px/32px 'Poppins',sans-serif;color:#444}

/* brands */
.brands{left:0;top:1274px;width:1200px;height:394px;background:var(--grey)}
.filter{position:absolute;top:1395px;height:47px;border:2px solid var(--pink);background:var(--white);font:400 16px 'Oswald',sans-serif;color:#333;display:flex;align-items:center;justify-content:center}
.filter.active{background:#333;border-color:#333;color:var(--white)}
.client{position:absolute;top:1512px;width:193px;height:95px;background:var(--white);border:3px solid #ddd;display:flex;align-items:center;justify-content:center;font:600 24px 'Poppins',sans-serif;color:#222}

/* quote */
.quote-text{left:200px;top:1866px;width:800px;text-align:center;font:300 35px/44px 'Poppins',sans-serif;color:var(--white);letter-spacing:.5px}

/* blog */
.post-img{position:absolute;top:2340px;width:329px;height:217px;border-radius:10px}
.post-title{position:absolute;top:2575px;width:320px;font:600 27px/35px 'Poppins',sans-serif;color:#333}
.post-more{position:absolute;top:2658px;font:500 19px 'Oswald',sans-serif;color:var(--pink);text-decoration:underline;text-underline-offset:3px}

/* footer */
.footer-col h4{position:absolute;top:2920px;font:400 21px 'Oswald',sans-serif;color:var(--white)}
.footer-link{position:absolute;font:400 15px 'Poppins',sans-serif;color:var(--white)}
.footer-small{position:absolute;font:400 13px/20px 'Poppins',sans-serif;color:var(--white)}
</style>
</head>
<body>

<!-- Header -->
<div class="brand" style="left:75px;top:29px">
  <div class="brand-dot"></div>
  <div class="brand-name">Brindle Media</div>
</div>
<nav class="nav">
  <a class="active" style="left:332px">HOME</a>
  <a style="left:409px">OUR WORK</a>
  <a style="left:534px">JOIN US</a>
  <a style="left:637px">BLOG</a>
  <a style="left:722px">8POINT2</a>
</nav>
<div class="abs contact-phone">
  <svg width="18" height="20" viewBox="0 0 24 24"><path d="M6.6 10.8a15 15 0 0 0 6.6 6.6l2.2-2.2c.3-.3.7-.4 1-.2 1.1.4 2.3.6 3.6.6.6 0 1 .4 1 1V20c0 .6-.4 1-1 1C10.6 21 3 13.4 3 4c0-.6.4-1 1-1h3.5c.6 0 1 .4 1 1 0 1.3.2 2.5.6 3.6.1.3 0 .7-.2 1z" fill="var(--pink)"/></svg>
  +44 20 7946 0312
</div>
<div class="abs contact-mail">
  <svg width="18" height="14" viewBox="0 0 24 18"><rect width="24" height="18" rx="2" fill="var(--pink)"/><path d="M1 2l11 8 11-8" stroke="#fff" stroke-width="2" fill="none"/></svg>
  hello@brindle-media.com
</div>

<!-- Hero -->
<section class="abs hero">
  <div class="hero-photo" role="img" aria-label="Photo of a woman working at a desk with a computer in a bright office"></div>
  <svg class="abs" style="left:0;top:0" width="1200" height="667" viewBox="0 0 1200 667">
    <path d="M0 450 Q560 820 1200 480 L1200 667 L0 667 Z" fill="var(--pink)"/>
    <path d="M0 468 Q560 838 1200 498 L1200 667 L0 667 Z" fill="var(--white)"/>
  </svg>
</section>
<h1 class="abs hero-title">BRINDLE MEDIA</h1>
<p class="abs hero-sub">We are an award-winning, global media<br>planning and buying.</p>
<p class="abs hero-tag">NEVER STOP, NEVER SETTLE, BE AMAZING</p>
<a class="btn" style="left:75px;top:457px;width:165px;height:55px">READ MORE</a>
<div class="abs dots"><i></i><i class="on"></i><i></i><i></i></div>

<!-- About -->
<div class="abs about-photo" role="img" aria-label="Group photo of the agency team at an office party"></div>
<p class="eyebrow" style="left:525px;top:857px">ABOUT US</p>
<h2 class="section-title" style="left:524px;top:880px">WHO WE ARE</h2>
<p class="abs about-copy">We are Brindle Media. We are an award-winning, global media planning and buying agency. We are a media agency for clients that want to drive real business change. We excel with clients who are visionary, innovative and driven, always ready to push boundaries and embrace new possibilities.</p>
<a class="btn" style="left:524px;top:1148px;width:165px;height:54px">READ MORE</a>

<!-- Brands -->
<section class="abs brands">
  <svg class="abs" style="left:0;top:0" width="1200" height="394" viewBox="0 0 1200 394"><polygon points="0,0 792,0 0,394" fill="var(--pink)"/></svg>
</section>
<p class="eyebrow" style="left:75px;top:1333px;color:var(--white)">WORK WITH US</p>
<h2 class="section-title" style="left:74px;top:1355px;color:var(--white)">OUR BRANDS</h2>
<p class="abs" style="left:75px;top:1434px;font:400 17px/27px 'Poppins',sans-serif;color:var(--white)">We work with some of the world's most<br>amazing brands.</p>
<div class="filter active" style="left:491px;width:213px">BEHAVIOUR CHANGE CLIENTS</div>
<div class="filter" style="left:714px;width:118px">B2B CLIENTS</div>
<div class="filter" style="left:842px;width:137px">CULTURE CLIENTS</div>
<div class="filter" style="left:989px;width:136px">RETAIL CLIENTS</div>
<svg class="abs" style="left:50px;top:1548px" width="14" height="24" viewBox="0 0 14 24"><path d="M12 2L2 12l10 10" stroke="#333" stroke-width="2" fill="none"/></svg>
<div class="client" style="left:75px">Fernway</div>
<div class="client" style="left:289px">Loopa</div>
<div class="client" style="left:504px">Civic Stage</div>
<div class="client" style="left:719px">Pingwell</div>
<div class="client" style="left:934px;font-size:20px">Stage at Home</div>
<svg class="abs" style="left:1134px;top:1548px" width="14" height="24" viewBox="0 0 14 24"><path d="M2 2l10 10L2 22" stroke="var(--pink)" stroke-width="2" fill="none"/></svg>

<!-- Quote -->
<svg class="abs" style="left:0;top:1715px" width="1200" height="440" viewBox="0 0 1200 440" role="img" aria-label="Photo of a woman with glasses looking upward, tinted red and teal">
  <defs>
    <linearGradient id="quoteFill" x1="0" y1="0" x2="1" y2="0">
      <stop offset="0" stop-color="#b5524a"/><stop offset=".45" stop-color="#7a4a48"/><stop offset=".6" stop-color="#3f5a60"/><stop offset="1" stop-color="#435a62"/>
    </linearGradient>
  </defs>
  <path d="M75 78 Q600 -60 1125 170 L1125 355 Q600 520 75 230 Z" fill="var(--pink)"/>
  <path d="M75 92 Q600 -38 1125 188 L1125 343 Q600 500 75 214 Z" fill="url(#quoteFill)"/>
</svg>
<p class="abs quote-text">Doing the same as everyone else,will get<br>you the same results as<br>everyone else.</p>

<!-- Blog -->
<p class="eyebrow" style="left:74px;top:2214px">BLOG POSTS</p>
<h2 class="section-title" style="left:73px;top:2236px">RESOURCES</h2>
<svg class="abs" style="left:1055px;top:2247px" width="26" height="22" viewBox="0 0 26 22"><path d="M24 11H3M12 2L3 11l9 9" stroke="#222" stroke-width="3" fill="none"/></svg>
<svg class="abs" style="left:1101px;top:2247px" width="26" height="22" viewBox="0 0 26 22"><path d="M2 11h21M14 2l9 9-9 9" stroke="var(--pink)" stroke-width="3" fill="none"/></svg>

<div class="post-img" style="left:75px;background:linear-gradient(135deg,#5a4a42,#c9c2b8)" role="img" aria-label="Photo of colleagues reviewing notes on a glass wall"></div>
<div class="post-img" style="left:436px;background:linear-gradient(135deg,#8a6a48,#c7b8a6)" role="img" aria-label="Photo of a woman on a laptop with social media icons around her"></div>
<div class="post-img" style="left:797px;background:linear-gradient(135deg,#4a5560,#b58a4e)" role="img" aria-label="Photo of hands holding a tablet over a desk with a keyboard"></div>
<h3 class="post-title" style="left:74px">B2B Marketing in 2024 and beyond..</h3>
<h3 class="post-title" style="left:436px">B2B Marketing in 2024 and beyond..</h3>
<h3 class="post-title" style="left:797px">B2B Marketing in 2024 and beyond..</h3>
<a class="post-more" style="left:74px">READ MORE</a>
<a class="post-more" style="left:436px">READ MORE</a>
<a class="post-more" style="left:797px">READ MORE</a>

<!-- Footer -->
<svg class="abs" style="left:0;top:2760px" width="1200" height="440" viewBox="0 0 1200 440">
  <path d="M0 100 Q560 -40 1200 86 L1200 440 L0 440 Z" fill="var(--pink)"/>
  <path d="M0 110 Q560 -28 1200 96 L1200 440 L0 440 Z" fill="var(--ink)"/>
</svg>
<div class="brand on-dark" style="left:75px;top:2930px">
  <div class="brand-dot" style="width:76px;height:76px"></div>
  <div class="brand-name" style="font-size:21px">Brindle Media</div>
</div>
<p class="footer-small" style="left:75px;top:3040px">Copyright © 2024 Brindle media.<br>All Rights Reserved.</p>
<p class="footer-small" style="left:75px;top:3096px">Registered in England &amp; Wales</p>
<p class="footer-small" style="left:75px;top:3119px;color:var(--pink)">No. 04417265</p>

<div class="footer-col">
  <h4 style="left:375px">SITE MAP</h4>
  <h4 style="left:603px">QUICK LINKS</h4>
  <h4 style="left:831px">GET IN TOUCH</h4>
</div>
<span class="footer-link" style="left:375px;top:2966px">Home</span>
<span class="footer-link" style="left:375px;top:3004px">Blog</span>
<span class="footer-link" style="left:375px;top:3043px">Our Work</span>
<span class="footer-link" style="left:375px;top:3081px">Join Us</span>
<span class="footer-link" style="left:375px;top:3120px">8point2</span>
<span class="footer-link" style="left:603px;top:2966px">Privacy Policy</span>
<span class="footer-link" style="left:603px;top:3004px">Join Us</span>
<span class="footer-link" style="left:603px;top:3043px">Our Services</span>

<p class="footer-small" style="left:831px;top:2953px;font-size:12.5px">Be brave, be different, get in touch.</p>
<svg class="abs" style="left:831px;top:2995px" width="15" height="14" viewBox="0 0 24 22"><path d="M1 4l7-3 8 3 7-3v17l-7 3-8-3-7 3z" fill="var(--pink)"/></svg>
<p class="footer-small" style="left:860px;top:2990px;font-size:14.5px;line-height:23px">2nd Floor, 18 Larkmead Row,<br>London, E2 7QT</p>
<svg class="abs" style="left:831px;top:3053px" width="13" height="14" viewBox="0 0 24 24"><path d="M6.6 10.8a15 15 0 0 0 6.6 6.6l2.2-2.2c.3-.3.7-.4 1-.2 1.1.4 2.3.6 3.6.6.6 0 1 .4 1 1V20c0 .6-.4 1-1 1C10.6 21 3 13.4 3 4c0-.6.4-1 1-1h3.5c.6 0 1 .4 1 1 0 1.3.2 2.5.6 3.6.1.3 0 .7-.2 1z" fill="var(--pink)"/></svg>
<p class="footer-small" style="left:860px;top:3051px;font-size:14.5px">+44 20 7946 0312</p>
<svg class="abs" style="left:831px;top:3093px" width="15" height="11" viewBox="0 0 24 18"><rect width="24" height="18" rx="2" fill="var(--pink)"/><path d="M1 2l11 8 11-8" stroke="#151515" stroke-width="2" fill="none"/></svg>
<p class="footer-small" style="left:864px;top:3089px;font-size:14.5px">hello@brindle-media.com</p>
<div class="abs" style="left:831px;top:3134px;display:flex;align-items:center;gap:8px">
  <span style="width:20px;height:20px;background:var(--pink);display:block"></span>
  <span style="font:400 14px 'Poppins',sans-serif;color:var(--white)">Netlinker</span>
</div>

</body>
</html>
```